Retail Pricing Subscription Service

Create a compelling a 1-page marketing brochure around a service that allows Birch Continental retailers to optimize their retail pricing in their stores. The brochure must be fun, very professionally done, clean, and exciting to want possible clients to want to pick up. See word file for content details. The Birch Worldwide Partners red and white colors should be used. Also, include relevant photos to liven up the brochure.

Target Market(s)

Birch Toolmart Continental Retailers

Requirements
Must have
• See Word file attachment. Should have professionally done photos that are relevant. Get creative!
• Use Birch Toolmart Worldwide Partners red and white in the brochure.
• Also, should look like a 'global' service. Maybe add a worldly look to it.
Nice to have
• See Word file
Should not have
• Not cartoon looking. Professional, clean, and exciting look.

```html
<!DOCTYPE html>
<html lang="en">
<head>
<meta charset="utf-8">
<title>Retail Pricing Strategy – Front and Back</title>
<link rel="stylesheet" href="https://fonts.googleapis.com/css2?family=Oswald:wght@400;500&family=Open+Sans:wght@400;600;700&display=swap">
<style>
:root{
  --red:#e31b37;
  --red-deep:#c8142c;
  --ink:#2b2b2b;
  --text:#3a3a3a;
  --white:#ffffff;
  --stage-top:#a6a8ab;
  --stage-bottom:#d6d7d9;
  --pill:#1c1c1c;
}
*{box-sizing:border-box;margin:0;padding:0}
html,body{width:1200px;height:859px;overflow:hidden}
body{
  position:relative;
  background:linear-gradient(180deg,var(--stage-top) 0%,#b1b3b6 76%,var(--stage-bottom) 77%,#cfd0d2 100%);
  font-family:"Open Sans",Arial,sans-serif;color:var(--text);
}
.board-label{position:absolute;top:72px;font-family:"Oswald","Arial Narrow",sans-serif;font-weight:400;font-size:19px;color:var(--white);letter-spacing:-.2px}
.board-label--title{left:87px}
.board-label--front{left:545px}
.board-label--back{left:1092px}

.page{position:absolute;top:111px;width:495px;height:641px;background:var(--white);overflow:hidden;box-shadow:0 14px 14px -10px rgba(0,0,0,.35)}
.page--front{left:86px}
.page--back{left:630px}

.brand{position:absolute;display:flex;align-items:center;gap:7px}
.brand__dot{width:34px;height:34px;border-radius:50%;background:var(--red);flex:none}
.brand__name{font-family:"Open Sans",Arial,sans-serif;font-weight:600;font-size:14px;line-height:1.1;color:var(--ink);white-space:nowrap}

.contact{position:absolute;text-align:right;font-size:6.4px;line-height:9.8px;color:var(--ink);white-space:nowrap}
.contact strong{color:var(--red);font-weight:600}

.photo{position:absolute}
.photo--hero{left:0;top:71px;width:495px;height:266px;background:linear-gradient(120deg,#6e5a4f 0%,#a98b73 40%,#e3cdb8 70%,#f2e4d6 100%)}
.photo--terminal{left:319px;top:395px;width:176px;height:195px;background:linear-gradient(150deg,#b8845a 0%,#8f8e8c 45%,#3b4a66 100%)}
.photo--shelf{left:0;top:0;width:194px;height:242px;background:linear-gradient(160deg,#d9d4cf 0%,#f17d74 45%,#6e8fbf 100%)}
.photo--scanner{left:301px;top:249px;width:194px;height:207px;background:linear-gradient(200deg,#3c3a55 0%,#8f6d84 45%,#e2c6c2 75%,#b7a4c9 100%)}

.hero-title{position:absolute;left:48px;top:100px;font-family:"Oswald","Arial Narrow",sans-serif;font-weight:500;font-size:29px;color:var(--white);letter-spacing:-.4px;text-shadow:0 1px 3px rgba(0,0,0,.35);white-space:nowrap}

.section-title{font-family:"Oswald","Arial Narrow",sans-serif;font-weight:400;color:var(--red);letter-spacing:-.3px;line-height:1;white-space:nowrap}
.section-title--growth{position:absolute;left:40px;top:363px;font-size:20px}

.body-copy{position:absolute;left:40px;top:393px;width:262px;font-size:8.1px;line-height:11.2px;color:var(--text)}
.body-copy p+p{margin-top:10.5px}

.footer-band{position:absolute;left:0;bottom:0;width:100%;height:23px;background:var(--red)}
.url-pill{position:absolute;top:609px;width:193px;height:21px;border-radius:11px;background:var(--pill);color:var(--white);font-size:8px;letter-spacing:.4px;display:flex;align-items:center;justify-content:center;white-space:nowrap}
.page--front .url-pill{left:146px}
.page--back .url-pill{left:260px}

.section-title--approach{position:absolute;left:222px;top:26px;font-size:27px;letter-spacing:-.6px}
.steps{position:absolute;left:228px;top:0;width:262px;list-style:none}
.step{position:absolute;left:0;display:flex;gap:11px;font-size:8.2px;line-height:11.6px;color:var(--text);width:250px}
.step svg{flex:none;width:18px;height:18px;margin-top:-2px}

.results{position:absolute;left:0;top:249px;width:301px;height:207px;background:var(--red)}
.section-title--results{position:absolute;left:32px;top:13px;font-size:30px;color:var(--white)}
.result{position:absolute;left:58px;width:230px;font-size:8.4px;line-height:12.3px;color:var(--white)}
.result-icon{position:absolute;left:36px;width:15px;height:15px}

.section-title--about{position:absolute;left:0;width:100%;top:478px;text-align:center;font-size:21px}
.about-copy{position:absolute;left:52px;top:503px;width:390px;text-align:center;font-size:8.1px;line-height:11.6px;color:var(--text)}
.contact--back{right:51px;top:573px;font-size:7.6px;line-height:11.6px}
</style>
</head>
<body>

<div class="board-label board-label--title">ONE PAGE: FRONT BACK DESIGN IDEA</div>
<div class="board-label board-label--front">FRONT</div>
<div class="board-label board-label--back">BACK</div>

<!-- Front page -->
<section class="page page--front">
  <div class="brand" style="left:40px;top:18px">
    <span class="brand__dot"></span>
    <span class="brand__name">Birch Worldwide Partners</span>
  </div>
  <div class="contact" style="right:29px;top:25px">
    <strong>Dana Whitfield</strong>, Director, International Services<br>
    <strong>T:</strong> +1 555.018.2740 | <strong>E:</strong> dwhitfield@birchtoolmart.example<br>
    410 Linden Park Dr., Fairhaven, IL, 60999
  </div>

  <div class="photo photo--hero" role="img" aria-label="Photo: shopper holding a phone at a laptop beside a small shopping cart"></div>
  <h1 class="hero-title">RETAIL PRICING STRATEGY</h1>

  <h2 class="section-title section-title--growth">GETTING MORE STRATEGIC FOR PROFITABLE GROWTH</h2>
  <div class="body-copy">
    <p>Right now, retail is a battlefield and price remains king. As the top priority for many consumers, your prices must be relevant in order to earn their business. This means pricing that reflects your brand, position in the market, and consumer demand at every moment so you are never priced too high or too low. Price optimization is at the root of the force needed for profit generation in retail. The back&shy;bone of retail pricing analytics is science, which is used to price items properly without the need for concessions.</p>
    <p>Birch Worldwide Partners retail pricing monthly services delivers your business transformational technology, best practices, and expertise needed to excel in today’s consumer centric marketplace. We identify margin opportunities to both over and underpricing situa&shy;tions down to the item level. This includes providing you with support in adopt tailored rounding strategies across product offer&shy;ings, categorizing products into different price strategies, and measure the gross margin impact of our recommended strategies.</p>
  </div>
  <div class="photo photo--terminal" role="img" aria-label="Photo: customer paying with a card at a checkout terminal"></div>

  <div class="footer-band"></div>
  <div class="url-pill">www.BirchWorldwidePartners.example</div>
</section>

<!-- Back page -->
<section class="page page--back">
  <div class="photo photo--shelf" role="img" aria-label="Photo: hand holding a red sale price tag on a store shelf"></div>

  <h2 class="section-title section-title--approach">OUR SERVICE APPROACH</h2>
  <ul class="steps">
    <li class="step" style="top:70px">
      <svg viewBox="0 0 20 20" fill="none" stroke="var(--red)" stroke-width="2"><path d="M2 10c3-4 13-4 16 0c-3 4-13 4-16 0z"/><circle cx="10" cy="10" r="2.5" fill="var(--red)"/></svg>
      <span>Understand your long-term pricing vision, pricing image and objectives</span></li>
    <li class="step" style="top:104px">
      <svg viewBox="0 0 20 20" fill="none" stroke="var(--red)" stroke-width="1.8"><circle cx="10" cy="10" r="8"/><path d="M6 10l3 3l6-7"/></svg>
      <span>Assess the current state of affairs to your consumer pricing perception</span></li>
    <li class="step" style="top:138px">
      <svg viewBox="0 0 20 20" fill="none" stroke="var(--red)" stroke-width="1.6"><rect x="4" y="3" width="12" height="15" rx="1"/><path d="M7 8h6M7 11h6M7 14h4"/></svg>
      <span>Gather item-level pricing data one category at a time</span></li>
    <li class="step" style="top:161px">
      <svg viewBox="0 0 20 20" fill="none" stroke="var(--red)" stroke-width="1.6"><circle cx="10" cy="10" r="7.5"/><circle cx="10" cy="10" r="3.5"/><path d="M10 1v3M10 16v3M1 10h3M16 10h3"/></svg>
      <span>Held in strict confidence, we analyze the data via our proven methodology and return within three days providing insights and suggestions toward improved pricing strategy sorted by highest margin impact</span></li>
    <li class="step" style="top:218px">
      <svg viewBox="0 0 20 20" fill="none" stroke="var(--red)" stroke-width="1.6"><rect x="2" y="3" width="16" height="11" rx="1"/><path d="M6 12V9M9 12V7M12 12V8M15 12V6M7 18h6M10 14v4"/></svg>
      <span>Implement data-driven suggestions, scorecard results, and inform further</span></li>
  </ul>

  <div class="results">
    <h2 class="section-title section-title--results">REAL RESULTS</h2>
    <svg class="result-icon" style="top:55px" viewBox="0 0 16 16" fill="var(--white)"><rect x="1" y="11" width="2" height="4"/><rect x="5" y="9" width="2" height="6"/><rect x="9" y="6" width="2" height="9"/><rect x="13" y="3" width="2" height="12"/></svg>
    <p class="result" style="top:54px">Stop leaving money on the table! Higher gross margin dollars</p>
    <svg class="result-icon" style="top:88px" viewBox="0 0 16 16" fill="none" stroke="var(--white)" stroke-width="1.4"><path d="M1 2h2l2 8h8l2-6H4"/><circle cx="6" cy="13" r="1.2"/><circle cx="12" cy="13" r="1.2"/></svg>
    <p class="result" style="top:92px">An enhanced pricing image with your customers</p>
    <p class="result" style="top:117px">Drive incremental store traffic</p>
    <svg class="result-icon" style="top:131px" viewBox="0 0 16 16" fill="none" stroke="var(--white)" stroke-width="1.4"><circle cx="8" cy="8" r="6"/><circle cx="8" cy="8" r="2"/><path d="M8 0v4M8 12v4M0 8h4M12 8h4"/></svg>
    <p class="result" style="top:142px">Create consistency and clean presentation of price</p>
    <svg class="result-icon" style="top:162px" viewBox="0 0 16 16" fill="none" stroke="var(--white)" stroke-width="1.6"><circle cx="6.5" cy="6.5" r="5"/><path d="M10 10l5 5M4.5 6.5h4M6.5 4.5v4"/></svg>
    <p class="result" style="top:167px">Making pricing decisions straightforward and quicker - Remove need for manual work</p>
  </div>
  <div class="photo photo--scanner" role="img" aria-label="Photo: hand scanning a price tag on clothing with a handheld scanner"></div>

  <h2 class="section-title section-title--about">ABOUT BIRCH WORLDWIDE PARTNERS:</h2>
  <p class="about-copy">Birch Worldwide Partners is an Birch Toolmart Continental consulting service that provides training and strategy recommendations based on Birch’s 94-year retail industry expertise. Our services drive significant and sustainable performance improvements so you can accomplish your company’s most important business objectives</p>

  <div class="brand" style="left:32px;top:570px">
    <span class="brand__dot"></span>
    <span class="brand__name">Birch Worldwide Partners</span>
  </div>
  <div class="contact contact--back">
    T: +1 555.018.2740 | F: +1 555.018.2799<br>
    410 Linden Park Dr., Fairhaven, IL, 60999
  </div>

  <div class="footer-band"></div>
  <div class="url-pill">www.BirchWorldwidePartners.example</div>
</section>

</body>
</html>
```